WordPress design for BraxtonVell.com

*****
OVERVIEW
*****
BraxtonVell.com needs a fresh, clean, professional design that effectively illustrates its talent in a thoughtful, impressive, and impactful way.
Vell Architecture & Interiors (www.braxtonvell.com) is a well-established, prestigious, well-publicized New England USA architecture firm. Founded in 1996, the privately-held company specializes in high-end residential projects with a focus on classic New England style architecture.
Business contact information is as noted below:
Address:
Vell Architecture & Interiors
87 Orchard Terrace
Needham, MA 02817
Telephone:
617-555-0138
781-555-0274
Email:
info@braxtonvell.com
An excerpt from the current site describes the outfit with this:
"Our architecture and interior design practices are centered around the philosophy that successful living spaces combine a focus on richly articulated detail and an in-depth knowledge of quality construction techniques."
*****
DESIGN RESEARCH
*****
In reviewing design ideas, the following sites were appealing:
Good
- Marcus Thorne Architects (http://mtaarchitects-example.com/) - Simple and clean, but almost too simple.
Better
- Penrose Galt Architecture (http://www.penrosegalt-example.com/) - Direct portfolio access. Simple and clean.
Best
- Brimwell Architects (http://www.brimwellarchitects-example.com/) - Clean, simple, easy to navigate
- QRV Architecture & Interiors (http://www.qrv-architects-example.com/) - Excellent use of high-resolution media, transitions, and navigation.
Here is an example of what is NOT desired:
Tolland Pryce Architects (http://www.tollandpryce-example.com/) - Cluttered, tight landing page. Uncertain navigation.
*****
OTHER DETAILS
*****
The grey in the Vell Architecture & Interiors logo is hex 636363. The font is unknown.
Updates
Project Deadline Extended
Reason: Hello everyone,
Thank you for your continued patience with this project. As it turns out, a critical member of the decision making team on our client's end has been out of the office this week. She will be back next week and is ready to be fully engaged with this. That said, we are extending the contest for at least 5 days. Next week will be much more active.
Thank you for your understanding.
Glasswick Technology Services
Project Deadline Extended
Reason: Hello everyone,
The customer was on vacation and only returned Monday of this week. That said, we need to extend the deadline for 5 days to afford time for review and comment.
Thank you for your patience! The designs submitted thus far are fantastic!
Thanks again,
Project Deadline Extended
Reason: Hello,
With so many designs, the customer is taking longer than anticipated to review them. They are looking at them offline and will process a large batch of comments when ready.
That said, the contest is being extended again.
Thank you for your continued patience.
Project Deadline Extended
Reason: Hello,
Because there are 108 designs to review and comment on, this is taking much longer than anticipated. That said, the contest is being extended another 5 days to ensure the customer has the desired outcome.
Thank you,
Target Market(s)
- Would-be clients
- Landowners
- Construction firms and general contractors
- High-end residential component manufacturers
- Media outlets
- All others interested in high-end residential architecture and interior design
Industry/Entity Type
Architecture
Requirements
Must have
- - Lots of media capabilities, such as embedded video (via ClipStream is fine), project image gallery, sliders for various functions, and social media integrations
- - At least one large slider on the landing page is critical, as well as space for standard lead-in things, such as news/events, opportunities, project highlights, and the likes
- - A high-resolution project showcase - finished projects and works in progress - is critical
- - A place to highlight business partners with the potential for reciprocation
- Form capabilities for things like information requests and general contacts from the public
- - Design must be handed off in a logically-layered (for WordPress) PSD with any and all additional source files provided (e.g. Photoshop, Illustrator, fonts, etc)
Nice to have
- - The WordPress design should be capable of fitting into the very popular FernLayouts Trellis theme.

```html
<!DOCTYPE html>
<html lang="en">
<head>
<meta charset="utf-8">
<title>Vell Architecture &amp; Interiors</title>
<link rel="stylesheet" href="https://fonts.googleapis.com/css2?family=Open+Sans:wght@300;400;600;700&display=swap">
<style>
:root{
  --red:#e0312c;
  --dark:#363636;
  --darker:#2b2b2b;
  --ink:#333333;
  --muted:#8a8a8a;
  --line:#e2e2e2;
  --white:#ffffff;
  --logo-grey:#636363;
}
*{box-sizing:border-box;margin:0;padding:0}
html,body{width:1200px;height:4088px;overflow:hidden}
body{font-family:"Open Sans",Arial,sans-serif;color:var(--ink);background:var(--white);font-size:12px;line-height:1.6;position:relative}
section,header,footer{position:absolute;left:0;width:1200px}
.abs{position:absolute}
p{color:var(--muted)}

/* hero */
.hero{top:0;height:592px;background:linear-gradient(180deg,#1d2c44 0%,#2f4766 40%,#6b5a45 62%,#2a3540 78%,#16232e 100%)}
.hero-glow{position:absolute;left:330px;top:220px;width:560px;height:170px;background:radial-gradient(ellipse at center,rgba(240,190,120,.55),rgba(240,190,120,0) 70%)}
.nav{position:absolute;top:0;left:0;width:1200px;height:56px;background:rgba(0,0,0,.35)}
.brand{position:absolute;left:120px;top:8px;color:var(--white)}
.brand-name{font-size:28px;font-weight:600;letter-spacing:3px;line-height:32px}
.brand-sub{font-size:8px;letter-spacing:2.5px;font-weight:600;text-transform:uppercase}
.menu{position:absolute;right:160px;top:20px;display:flex;gap:28px;list-style:none}
.menu li{color:var(--white);font-size:12px}
.menu li.active{color:var(--red)}
.hero-box{position:absolute;left:290px;top:280px;width:620px;height:120px;background:rgba(0,0,0,.45)}
.hero-title{position:absolute;top:286px;left:0;width:1200px;text-align:center;color:var(--white);font-size:34px;font-weight:700;letter-spacing:.5px}
.hero-text{position:absolute;top:338px;left:340px;width:520px;text-align:center;color:#e6e6e6;font-size:12px;line-height:17px}
.btn-red{position:absolute;background:var(--red);color:var(--white);font-size:12px;font-weight:600;text-align:center;border-radius:2px}

/* services */
.services{top:592px;height:456px}
.section-title{position:absolute;left:0;width:1200px;text-align:center;font-size:28px;font-weight:300;color:var(--ink)}
.section-title b{font-weight:400}
.mark{background:var(--ink);color:var(--white);padding:0 6px}
.red{color:var(--red)}
.lead{position:absolute;left:220px;width:760px;text-align:center;font-size:13px;line-height:20px}
.service{position:absolute;top:188px;width:200px;text-align:center}
.service svg{display:block;margin:0 auto}
.service h3{font-size:14px;font-weight:600;margin-top:14px}
.service p{font-size:11px;line-height:16px;margin-top:8px}
.more{position:absolute;top:352px;width:200px;font-size:11px;border-top:1px solid var(--line);padding-top:10px;text-align:center;color:var(--ink)}

/* civilizations */
.civil{top:1048px;height:552px;background:var(--dark)}
.civil h2{position:absolute;top:32px;width:1200px;text-align:center;color:var(--white);font-size:26px;font-weight:600}
.civil h3{position:absolute;top:76px;width:1200px;text-align:center;color:#e6e6e6;font-size:20px;font-weight:300}
.btn-outline{position:absolute;border:1px solid #bbbbbb;color:var(--white);font-size:11px;text-align:center;text-transform:uppercase;letter-spacing:.5px}

/* about */
.about{top:1600px;height:680px}
.title-rule{position:absolute;left:560px;width:80px;height:2px;background:var(--red)}
.photo{position:absolute}
.about-copy{position:absolute;left:484px;top:120px;width:516px}
.about-copy p{font-size:11px;line-height:17px;margin-bottom:12px}
.feature-list{position:absolute;left:200px;top:340px;width:370px;list-style:none}
.feature-list li{position:relative;padding-right:30px;height:52px;border-bottom:1px solid var(--line);padding-top:8px}
.feature-list li strong{display:block;font-size:11px;font-weight:600}
.feature-list li span{font-size:10px;color:var(--muted)}
.feature-list li i{position:absolute;right:4px;top:20px;width:12px;height:12px;border-radius:50%;background:var(--ink)}
.tabs{position:absolute;left:596px;top:318px;width:404px;height:300px;border:1px solid var(--line)}
.tab-row{display:flex;border-bottom:1px solid var(--line);height:32px}
.tab-row span{font-size:10px;padding:8px 14px;border-right:1px solid var(--line);text-transform:uppercase;color:var(--muted)}
.tab-row span.on{color:var(--red);border-top:2px solid var(--red)}
.tab-body p{font-size:10px;line-height:15px}

/* testimonial */
.testimonial{top:2280px;height:340px;background:var(--dark);text-align:center}
.quote-mark{position:absolute;left:584px;top:28px}
.testimonial p{position:absolute;top:104px;left:220px;width:760px;color:#d8d8d8;font-size:12px;line-height:18px}
.testimonial .who{position:absolute;top:158px;width:1200px;color:var(--white);font-size:13px;font-weight:600}
.testimonial .role{position:absolute;top:184px;left:520px;width:160px;color:#bdbdbd;font-size:11px;border-top:1px solid #555;padding-top:4px}

/* blog */
.blog{top:2620px;height:680px;background:#f7f7f7}
.post{position:absolute;top:120px;width:384px;height:420px;background:var(--white);border:1px solid var(--line)}
.post h3{position:absolute;left:30px;top:194px;width:320px;font-size:16px;font-weight:700;line-height:22px;color:var(--ink)}
.post p{position:absolute;left:30px;top:258px;width:320px;font-size:11px;line-height:17px}
.post-meta{position:absolute;left:30px;right:30px;bottom:18px;border-top:1px solid var(--line);padding-top:10px;font-size:10px;display:flex;justify-content:space-between}

/* gallery */
.gallery{top:3300px;height:212px;display:flex}
.gallery div{width:240px;height:212px}

/* footer */
.site-footer{top:3512px;height:576px;background:var(--darker);color:#cfcfcf}
.social{position:absolute;top:84px;left:0;width:1200px;display:flex;justify-content:center;gap:16px}
.social span{width:34px;height:34px;border-radius:50%;background:var(--red)}
.col-head{position:absolute;top:176px;color:var(--white);font-size:12px;font-weight:600}
.site-footer p{color:#9a9a9a;font-size:10px;line-height:15px}
.foot-input{position:absolute;background:#444;height:26px}
.btn-small{position:absolute;background:var(--red);color:var(--white);font-size:9px;text-align:center;line-height:20px;height:20px;border-radius:2px}
.contact-list{position:absolute;left:836px;top:206px;list-style:none;font-size:10px;color:#a5a5a5;line-height:20px}
.foot-brand{position:absolute;left:836px;top:434px;color:var(--white)}
.copyright{position:absolute;left:836px;top:482px;font-size:9px;color:#8d8d8d}
</style>
</head>
<body>

<header class="hero">
  <div class="hero-glow" role="img" aria-label="Modern stone villa with lit interiors beside a pool at dusk"></div>
  <nav class="nav">
    <div class="brand">
      <div class="brand-name">VELL</div>
      <div class="brand-sub">Architecture &amp; Interiors</div>
    </div>
    <ul class="menu">
      <li class="active">Home</li><li>About</li><li>Services</li><li>Portfolio</li><li>Blog</li><li>Contact</li>
    </ul>
  </nav>
  <div class="hero-box"></div>
  <h1 class="hero-title">There are many variations of passages</h1>
  <p class="hero-text">Lorem ipsum is simply dummy text of the printing and typesetting industry. Lorem ipsum has been the industry's standard dummy text ever since the 1500s, when an unknown printer took a galley of type and scrambled it to make a type specimen book.</p>
  <div class="btn-red" style="left:545px;top:412px;width:110px;height:30px;line-height:30px">Read More</div>
</header>

<section class="services">
  <h2 class="section-title" style="top:56px">We are <span class="mark">building</span> for the future.</h2>
  <p class="lead" style="top:104px">Lorem ipsum dolor sit amet, consectetur adipiscing elit. Etiam sed cursus sit lorem. Phasellus semper magna justo. Nulla pharetra metus a tincidunt elementum. Donec vel neque diam, ut aliquet feugiat est, a lacinia orci rhoncus ac.</p>

  <div class="service" style="left:160px">
    <svg width="62" height="70" viewBox="0 0 62 70"><polygon points="31,0 62,17.5 62,52.5 31,70 0,52.5 0,17.5" fill="var(--red)"/><rect x="18" y="24" width="26" height="16" rx="3" fill="#fff"/><polygon points="24,40 24,47 31,40" fill="#fff"/></svg>
    <h3>Consulting</h3>
    <p>Curabitur tortor lorem, aliquam vitae dapibus eget, lobortis ut nisl, ac tempus metus sed diam nonummy.</p>
  </div>
  <div class="more" style="left:160px">read more</div>

  <div class="service" style="left:380px">
    <svg width="62" height="70" viewBox="0 0 62 70"><polygon points="31,0 62,17.5 62,52.5 31,70 0,52.5 0,17.5" fill="var(--red)"/><rect x="17" y="30" width="28" height="10" fill="#fff"/><line x1="22" y1="30" x2="22" y2="35" stroke="var(--red)" stroke-width="1.5"/><line x1="28" y1="30" x2="28" y2="35" stroke="var(--red)" stroke-width="1.5"/><line x1="34" y1="30" x2="34" y2="35" stroke="var(--red)" stroke-width="1.5"/><line x1="40" y1="30" x2="40" y2="35" stroke="var(--red)" stroke-width="1.5"/></svg>
    <h3>Planning</h3>
    <p>Praesent vitae lorem ac purus porta fermentum, in lacinia tellus sed ante blandit gravida ultrices.</p>
  </div>
  <div class="more" style="left:380px">read more</div>

  <div class="service" style="left:600px">
    <svg width="62" height="70" viewBox="0 0 62 70"><polygon points="31,0 62,17.5 62,52.5 31,70 0,52.5 0,17.5" fill="var(--red)"/><polygon points="38,20 44,26 27,43 20,45 22,38" fill="#fff"/></svg>
    <h3>Design</h3>
    <p>Vivamus nullam dapibus tempor commodo felis, mauris viverra sed urna quis, pulvinar dictum lorem.</p>
  </div>
  <div class="more" style="left:600px">read more</div>

  <div class="service" style="left:820px">
    <svg width="62" height="70" viewBox="0 0 62 70"><polygon points="31,0 62,17.5 62,52.5 31,70 0,52.5 0,17.5" fill="var(--red)"/><rect x="21" y="22" width="20" height="26" fill="#fff"/><rect x="25" y="26" width="4" height="4" fill="var(--red)"/><rect x="33" y="26" width="4" height="4" fill="var(--red)"/><rect x="25" y="34" width="4" height="4" fill="var(--red)"/><rect x="33" y="34" width="4" height="4" fill="var(--red)"/><rect x="29" y="42" width="4" height="6" fill="var(--red)"/></svg>
    <h3>Building</h3>
    <p>Donec sodales sagittis magna, sed consequat leo eget bibendum sodales, augue velit cursus nunc quis.</p>
  </div>
  <div class="more" style="left:820px">read more</div>
</section>

<section class="civil">
  <h2>We used to build civilizations.</h2>
  <h3>Now we build shopping malls.</h3>
  <svg class="abs" style="left:210px;top:132px" width="780" height="272" viewBox="0 0 780 272">
    <defs>
      <linearGradient id="hexA" x1="0" y1="0" x2="1" y2="1"><stop offset="0" stop-color="#cfe0ea"/><stop offset="1" stop-color="#7d8f98"/></linearGradient>
      <linearGradient id="hexB" x1="0" y1="0" x2="1" y2="1"><stop offset="0" stop-color="#d9c9c6"/><stop offset="1" stop-color="#5a4a48"/></linearGradient>
      <linearGradient id="hexC" x1="0" y1="0" x2="1" y2="1"><stop offset="0" stop-color="#ece5dc"/><stop offset="1" stop-color="#8a7866"/></linearGradient>
    </defs>
    <polygon role="img" aria-label="Bright living room with floor-to-ceiling glass walls" points="118,0 236,68 236,204 118,272 0,204 0,68" fill="url(#hexA)"/>
    <polygon role="img" aria-label="Contemporary interior with warm lighting" points="390,0 508,68 508,204 390,272 272,204 272,68" fill="url(#hexB)"/>
    <polygon role="img" aria-label="Curved staircase in a modern hall" points="662,0 780,68 780,204 662,272 544,204 544,68" fill="url(#hexC)"/>
  </svg>
  <div class="btn-outline" style="left:534px;top:460px;width:132px;height:34px;line-height:32px">Discover more</div>
</section>

<section class="about">
  <h2 class="section-title" style="top:56px">About <span class="red">us</span></h2>
  <div class="title-rule" style="top:104px"></div>
  <div class="photo" role="img" aria-label="Abstract curved architecture against a sunset sky" style="left:200px;top:120px;width:252px;height:168px;background:linear-gradient(135deg,#f0b27a 0%,#a45a3a 55%,#3c2a26 100%)"></div>
  <div class="about-copy">
    <p>Lorem ipsum dolor sit amet, consectetur adipiscing elit. Vivamus et mi sed leo gravida pretium. Nunc condimentum elementum arcu, in fermentum eros imperdiet eget. Sed id ipsum at nibh faucibus iaculis et quis augue. Phasellus sed dui nec urna feugiat tristique.</p>
    <p>Cras sed ipsum posuere lorem fermentum dictum. Praesent vel nisi eget nunc tempus hendrerit. Fusce tincidunt lacus nec diam rhoncus, sed consequat erat vehicula. Suspendisse potenti nulla ut ipsum luctus, vitae placerat urna fringilla. Curabitur pretium mi eu metus dapibus.</p>
  </div>
  <ul class="feature-list">
    <li><strong>Lorem ipsum dolor sit amet</strong><span>Suspendisse et nisi vel dolor ultrices tincidunt.</span><i></i></li>
    <li><strong>Consectetur adipiscing elit</strong><span>Integer porta nibh at velit blandit volutpat.</span><i></i></li>
    <li><strong>Praesent sed tellus</strong><span>Aenean vitae sem sit amet mi pretium cursus.</span><i></i></li>
    <li><strong>Suspendisse et volutpat ante</strong><span>Morbi vel felis ut arcu finibus gravida.</span><i></i></li>
    <li><strong>Maecenas mollis lorem congue</strong><span>Donec at lectus id orci lacinia pretium.</span><i></i></li>
  </ul>
  <div class="tabs">
    <div class="tab-row"><span class="on">Consulting &amp; Design</span><span>Interiors</span><span>Modern Approach</span></div>
    <div class="tab-body">
      <div class="photo" role="img" aria-label="Interior with round window" style="left:16px;top:48px;width:110px;height:96px;background:linear-gradient(135deg,#9a8b7c,#3f3832)"></div>
      <p class="abs" style="left:140px;top:46px;width:248px">Proin vehicula lorem eget tortor posuere, a aliquet mauris fermentum. Nullam aliquet risus at ligula pharetra, sit amet tempor arcu pulvinar. Sed ut sapien quam.</p>
      <p class="abs" style="left:140px;top:118px;width:248px">Nam scelerisque tellus a commodo fringilla, et vehicula magna eleifend.</p>
      <strong class="abs" style="left:16px;top:160px;font-size:10px;font-weight:600">Morbi suscipit, ac tellus in dolor</strong>
      <p class="abs" style="left:16px;top:180px;width:372px">Quisque ut vulputate dui. Aliquam erat volutpat. Pellentesque habitant morbi tristique senectus et netus et malesuada fames ac turpis egestas. Vestibulum ante ipsum primis in faucibus orci luctus et ultrices posuere cubilia curae; fusce dignissim metus at lacus tincidunt.</p>
    </div>
  </div>
</section>

<section class="testimonial">
  <svg class="quote-mark" width="32" height="32" viewBox="0 0 32 32"><circle cx="16" cy="16" r="15" fill="none" stroke="#999" stroke-width="1.5"/><text x="16" y="24" text-anchor="middle" font-family="Open Sans, sans-serif" font-size="18" fill="#ccc">&#8220;</text></svg>
  <p>Suspendisse at nisi quis ante, dictum in eleifend quis, vehicula eget pretium porta tempus lobortis. In ut massa. Quisque sed felis sollicitudin rhoncus pulvinar, eget mauris. Nam vestibulum lacus, sed mattis orci, pellentesque et felis. Integer at vehicula porttitor lorem a magna.</p>
  <div class="who">John Doe</div>
  <div class="role">General Manager | ABC Inc</div>
  <div class="abs" role="img" aria-label="Client portrait" style="left:558px;top:216px;width:84px;height:84px;border-radius:50%;background:#8a8a8a;border:3px solid #ffffff"></div>
</section>

<section class="blog">
  <h2 class="section-title" style="top:56px">From <span class="red">our blog</span></h2>
  <article class="post" style="left:208px">
    <div class="photo" role="img" aria-label="Minimal bedroom with large windows" style="left:0;top:0;width:382px;height:166px;background:linear-gradient(135deg,#e6e1da,#9c8c7a)"></div>
    <h3>Curabitur laoreet massa, vitae vestibulum purus.</h3>
    <p>Lorem ipsum dolor sit amet, consectetur adipiscing elit. Nulla facilisi. Suspendisse tincidunt dui vel nisl eleifend, nec egestas purus ornare. Integer sed lacus lorem. Donec at dolor mattis, dictum elit et, sodales nisi quam.</p>
    <div class="post-meta"><span>by admin</span><span>read more</span></div>
  </article>
  <article class="post" style="left:608px">
    <div class="photo" role="img" aria-label="Open-plan kitchen and dining area" style="left:0;top:0;width:382px;height:166px;background:linear-gradient(135deg,#d7d4cf,#5e5650)"></div>
    <h3>Pellentesque eget ante pretium, blandit magna eu.</h3>
    <p>Phasellus ultricies sapien vitae nibh tincidunt, sit amet ultrices erat blandit. Mauris quis ligula ut risus convallis volutpat. Aenean fringilla turpis sed nisl sagittis, in feugiat arcu aliquet lacus.</p>
    <div class="post-meta"><span>by admin</span><span>read more</span></div>
  </article>
  <div class="btn-outline" style="left:520px;top:590px;width:160px;height:34px;line-height:32px;color:var(--ink);background:#fff">Read our latest posts</div>
</section>

<section class="gallery">
  <div role="img" aria-label="Living room interior" style="background:linear-gradient(135deg,#b59a7c,#4a3a2c)"></div>
  <div role="img" aria-label="Modern house at night" style="background:linear-gradient(135deg,#3e4b5a,#c08a4a)"></div>
  <div role="img" aria-label="Bright kitchen" style="background:linear-gradient(135deg,#e8e6e2,#8f8a82)"></div>
  <div role="img" aria-label="Poolside terrace" style="background:linear-gradient(135deg,#7ca3c4,#5b4a3a)"></div>
  <div role="img" aria-label="Spiral staircase" style="background:linear-gradient(135deg,#f0ece6,#6c6660)"></div>
</section>

<footer class="site-footer">
  <div class="social"><span></span><span></span><span></span><span></span><span></span><span></span></div>

  <div class="col-head" style="left:200px">A little about us</div>
  <div class="abs" role="img" aria-label="Architect portrait" style="left:200px;top:212px;width:60px;height:60px;background:#6b6b6b"></div>
  <p class="abs" style="left:272px;top:208px;width:170px">Our architecture and interior design practices combine richly articulated detail with an in-depth knowledge of quality construction.</p>

  <div class="col-head" style="left:200px;top:360px">Subscribe to our newsletter</div>
  <div class="foot-input" style="left:200px;top:392px;width:190px"></div>
  <div class="btn-small" style="left:398px;top:395px;width:44px">Sign up</div>

  <div class="col-head" style="left:540px">Latest from our blog</div>
  <div class="abs" style="left:490px;top:212px;width:36px;height:36px;border-radius:50%;background:#555"></div>
  <p class="abs" style="left:540px;top:210px;width:200px">Curabitur laoreet massa, vitae vestibulum purus lorem.</p>
  <div class="btn-small" style="left:540px;top:248px;width:54px">Read more</div>
  <div class="abs" style="left:490px;top:300px;width:36px;height:36px;border-radius:50%;background:#555"></div>
  <p class="abs" style="left:540px;top:298px;width:200px">Pellentesque eget ante pretium, blandit magna eu.</p>
  <div class="btn-small" style="left:540px;top:336px;width:54px">Read more</div>

  <div class="col-head" style="left:836px">Get in touch</div>
  <ul class="contact-list">
    <li>87 Orchard Terrace</li>
    <li>Needham, MA 02817</li>
    <li>617-555-0138</li>
    <li>781-555-0274</li>
    <li>info@braxtonvell.com</li>
    <li>www.braxtonvell.com</li>
  </ul>

  <div class="foot-brand">
    <div class="brand-name">VELL</div>
    <div class="brand-sub">Architecture &amp; Interiors</div>
  </div>
  <div class="copyright">Copyright &copy; 2013 Vell Architecture &amp; Interiors. All rights reserved.</div>
</footer>

</body>
</html>
```